Mosquito Repellent Wet Wipes pacakage design

We are a mosquito repellent manufacturer under the brand name "Zest Guard". We have a product currently and are looking to make it more attractive.

Our product is a mosquito repellent wipe that can be applied on skin and clothing for protection against mosquitoes. It is going to be available in sachets. Customer age groups include ages 10-30 as well as Moms who are key decision makers.

We are looking for a friendly package in terms of color and appeal and a redesign of Zest Guard logo. I am attaching our current product pictures and brochure. Hope this gets you started. We are attaching information on the spray bottle.

Visit www.tolvanhealthworks.com for more details.

Package Dimension Folded : 80x60 mm
Package Dimension unfolded: 80 x 120 mm

Thank you
Varun
Updates

Project Deadline Extended Reason: Still not happy with the designs that are submitted. Like to see more designs. Added Thursday, February 18, 2016

Target Market(s)

General population with more focus on age groups 10-30 as well as Moms

Industry/Entity Type

Cosmetics

Requirements
Must have
• Statutory information should be provided on the product including Manufacturing address, ingredient name & bar code. I guess we can do this once the package is finalized

```html
<!DOCTYPE html>
<html lang="en">
<head>
<meta charset="utf-8">
<title>Zest Guard Insect Repellent Wipes – Sachet Artwork</title>
<link rel="stylesheet" href="https://fonts.googleapis.com/css2?family=Roboto+Condensed:ital,wght@0,400;0,700;1,400;1,700&family=Montserrat:wght@700&display=swap">
<style>
  :root {
    --bg: #f1f1f1;
    --sachet: #ffffff;
    --seal-line: #d9d9d9;
    --brand-blue: #00aeef;
    --leaf-green: #8dc63f;
    --ink: #3a3a3a;
    --white: #ffffff;
  }
  * { box-sizing: border-box; margin: 0; padding: 0; }
  html, body { width: 1200px; height: 1200px; overflow: hidden; }
  body {
    background: var(--bg);
    font-family: "Roboto Condensed", sans-serif;
    color: var(--ink);
    position: relative;
  }

  /* Standalone brand mark */
  .brand-lockup {
    position: absolute; left: 90px; top: 100px;
    display: flex; align-items: center; gap: 14px;
  }
  .brand-lockup .dot {
    width: 22px; height: 22px; border-radius: 50%; background: var(--brand-blue);
  }
  .brand-name {
    font-weight: 700; color: var(--brand-blue);
    font-size: 76px; line-height: 1; text-transform: uppercase; letter-spacing: 1px;
    white-space: nowrap;
  }

  /* Sachet panels */
  .sachet {
    position: absolute; top: 360px; width: 440px; height: 590px;
    background: var(--sachet);
    box-shadow: 0 18px 30px rgba(0,0,0,0.12);
  }
  .sachet.front { left: 215px; }
  .sachet.back { left: 690px; }
  .seal { position: absolute; left: 0; right: 0; height: 56px; }
  .seal.top { top: 0; }
  .seal.bottom { bottom: 0; }
  .seal span { display: block; height: 2px; background: var(--seal-line); margin: 7px 0; }

  /* Front */
  .company {
    position: absolute; left: 50px; top: 82px;
    display: flex; align-items: center; gap: 8px;
    font-size: 28px; font-weight: 700; color: var(--brand-blue);
    white-space: nowrap;
  }
  .company .dot { width: 14px; height: 14px; border-radius: 50%; background: var(--leaf-green); }
  .front .product-name {
    position: absolute; left: 0; right: 0; top: 150px; text-align: center;
    font-size: 78px; font-weight: 700; color: var(--brand-blue);
    text-transform: uppercase; line-height: 1; white-space: nowrap;
  }
  .front .product-type {
    position: absolute; left: 0; right: 0; top: 242px; text-align: center;
    font-family: "Montserrat", sans-serif; color: var(--brand-blue); line-height: 1.2;
  }
  .product-type .line1 { display: block; font-size: 32px; letter-spacing: 2px; }
  .product-type .line2 { display: block; font-size: 22px; letter-spacing: 1px; }
  .mascot {
    position: absolute; width: 100px; height: 62px; border-radius: 30px;
    background: linear-gradient(135deg, #4aa3df, #8dc63f);
  }
  .front .mascot { left: 300px; top: 318px; }
  .front .claims {
    position: absolute; right: 48px; top: 392px; text-align: right; line-height: 1.25;
  }
  .claims .carry { font-size: 22px; }
  .claims .diseases { font-size: 24px; font-weight: 700; }
  .claims .fresh { font-size: 16px; font-weight: 700; color: var(--leaf-green); margin-top: 8px; }
  .front .pill {
    position: absolute; right: 48px; top: 492px;
    background: var(--brand-blue); color: var(--white);
    font-size: 14px; font-weight: 700; padding: 4px 12px; border-radius: 14px;
    white-space: nowrap;
  }

  /* Back */
  .back .about {
    position: absolute; left: 40px; right: 40px; top: 80px;
    font-size: 15px; font-style: italic; line-height: 1.35;
  }
  .back .about strong { font-weight: 700; }
  .back .mini-brand {
    position: absolute; left: 40px; top: 200px;
    display: flex; align-items: center; gap: 14px;
  }
  .mini-brand .text .name {
    font-size: 44px; font-weight: 700; color: var(--brand-blue); text-transform: uppercase; line-height: 1;
    white-space: nowrap;
  }
  .mini-brand .text .type {
    font-family: "Montserrat", sans-serif; font-size: 13px; color: var(--brand-blue); letter-spacing: 1px;
  }
  .back .mascot { position: static; width: 60px; height: 40px; }
  .back .details {
    position: absolute; left: 40px; right: 40px; top: 300px;
    font-size: 15px; line-height: 1.4;
  }
  .details p { margin-bottom: 12px; }
  .details strong { font-weight: 700; font-style: italic; }
  .back .company { left: auto; right: 40px; top: 470px; font-size: 24px; }
</style>
</head>
<body>

  <div class="brand-lockup">
    <span class="dot"></span>
    <span class="brand-name">Zest Guard</span>
  </div>

  <section class="sachet front">
    <div class="seal top"><span></span><span></span><span></span><span></span></div>
    <div class="company"><span class="dot"></span>Tolvan Health</div>
    <h1 class="product-name">Zest Guard</h1>
    <div class="product-type">
      <span class="line1">INSECT</span>
      <span class="line2">REPELLENT WIPES</span>
    </div>
    <div class="mascot" role="img" aria-label="Cartoon mosquito character illustration"></div>
    <div class="claims">
      <div class="carry">Repels Mosquitoes that may carry</div>
      <div class="diseases">Malaria, Chikungunya &amp; Dengue</div>
      <div class="fresh">Light &amp; Fresh with OLIVE EXTRACTS</div>
    </div>
    <div class="pill">Long lasting protection - 1Wipe | 12cmx15cm</div>
    <div class="seal bottom"><span></span><span></span><span></span><span></span></div>
  </section>

  <section class="sachet back">
    <div class="seal top"><span></span><span></span><span></span><span></span></div>
    <p class="about"><strong>Our product is a mosquito repellent wipe</strong> that can be applied on skin and clothing for protection against mosquitoes. It is going to be available in sachets. Customer age groups include ages 10-30 as well as Moms who are key decision makers.</p>
    <div class="mini-brand">
      <div class="text">
        <div class="name">Zest Guard</div>
        <div class="type">INSECT REPELLENT WIPES</div>
      </div>
      <div class="mascot" role="img" aria-label="Small cartoon mosquito character illustration"></div>
    </div>
    <div class="details">
      <p><strong>Usage intstruction:</strong> that can be applied on skin and clothing for protection against mosquitoes. It is going to be available in sachets. Customer age groups include ages 10-30 as well as Moms who are key decision makers.</p>
      <p><strong>Ingredients:</strong> DEET 15% ; OTHERS 85%</p>
      <p><strong>Manufactured by:</strong> Tolvan Health.</p>
    </div>
    <div class="company"><span class="dot"></span>Tolvan Health</div>
    <div class="seal bottom"><span></span><span></span><span></span><span></span></div>
  </section>

</body>
</html>
```